Single Page Timetracking Dashboard Desktop App UI Design (Figma Link required)

Main Idea: a SaaS tool where employees can add their time and project in a playful way. There is a infographics and a list with tasks as well.

Based on the attached concept.png the brief is following:

- check the attached rough scribble
- add own ideas or change things if they add value
- Style: colourful, nerdy, professional saas, modern, beautiful, white space
- Quality expectation: inspiration1+2.png
- I will need a Figma link
- desktop only
- make something fresh and unique

Process:
I need to include 2-3 feedback rounds that will span probably around 7 days

Target Market(s)

Internal Business Tool for a Software Development Company

Industry/Entity Type

IT

Other font styles liked:
• Could be monospace, not a must though

Requirements
Must have
• At least one page; Figma Link to the design;
Nice to have
• Microinterations like drop-down, hover/active colors; functionality specifications
Should not have
• Mobile view

```html
<!DOCTYPE html>
<html lang="en">
<head>
<meta charset="utf-8">
<title>Time Tracking Dashboard</title>
<link href="https://fonts.googleapis.com/css2?family=Outfit:wght@300;400;500;600&display=swap" rel="stylesheet">
<style>
:root{
  --coral:#ff6b6b;
  --coral-soft:#ff9a9a;
  --orange:#fb8f1a;
  --orange-soft:#fecb8a;
  --navy:#1e1b4b;
  --ink:#26262e;
  --muted:#9a9aa5;
  --line:#ececf1;
  --chip:#f1f1f3;
  --card:#ffffff;
  --teal:#17b9a0;
  --yellow:#f8c51c;
  --amber:#f59e0b;
  --pink:#ec4899;
  --violet:#6366f1;
  --blue:#3b82f6;
  --shadow:0 8px 24px rgba(120,130,170,.14);
}
*{box-sizing:border-box;margin:0;padding:0}
html,body{width:935px;height:1200px;overflow:hidden;background:#fff}
body{font-family:"Outfit",sans-serif;color:var(--ink);position:relative}
.abs{position:absolute}
.sidebar{left:0;top:0;width:91px;height:1200px;background:linear-gradient(90deg,var(--coral),var(--coral-soft))}
.nav-icon{position:absolute;left:34px;width:24px;height:24px}
.nav-icon svg{width:24px;height:24px;stroke:#fff;fill:none;stroke-width:2;stroke-linecap:round;stroke-linejoin:round}
.greeting{left:161px;top:28px;font-size:14px;letter-spacing:.3px}
.greeting b{color:var(--coral);font-weight:500}
.page-title{left:161px;top:62px;font-size:18px;font-weight:500}
.bell{left:657px;top:40px}
.bell-dot{left:670px;top:38px;width:6px;height:6px;border-radius:50%;background:#f43f5e}
.avatar{left:711px;top:36px;width:24px;height:24px;border-radius:7px;background:linear-gradient(135deg,#c99a7c,#6f5a4a)}
.user-name{left:742px;top:36px;font-size:8px;font-weight:500}
.user-plan{left:742px;top:49px;font-size:6.5px;color:var(--blue)}
.user-chev{left:826px;top:42px}
.card{position:absolute;background:var(--card);border-radius:6px;box-shadow:var(--shadow)}
.tracker{left:161px;top:105px;width:449px;height:354px}
.today{left:625px;top:105px;width:225px;height:354px}
.cal-title{left:27px;top:27px;font-size:12px;font-weight:500}
.cal-nav{top:30px;font-size:11px;color:var(--muted)}
.toggle{left:27px;top:59px;width:205px;height:20px;border-radius:10px;background:#f4f4f6;font-size:8.5px}
.toggle span{position:absolute;top:0;height:20px;line-height:20px;text-align:center;border-radius:10px}
.toggle .week{left:0;width:103px}
.toggle .month{left:104px;width:101px;background:var(--coral);color:#fff;font-weight:500}
.day-head,.day-num{position:absolute;width:22px;margin-left:-11px;text-align:center}
.day-head{font-size:8px;color:var(--muted)}
.day-num{font-size:8px;height:16px;line-height:16px}
.day-num.active{background:var(--coral);color:#fff;border-radius:50%;width:17px;height:17px;line-height:17px;margin-left:-8.5px}
.cal-rule{left:31px;top:220px;width:201px;height:1px;background:var(--line)}
.dur{position:absolute;width:46px;height:25px;line-height:25px;text-align:center;font-size:9px;background:var(--chip);border-radius:3px}
.dur.sel{background:#fff;border:1px solid var(--coral);line-height:23px}
.select{left:267px;width:160px;height:39px;border-radius:4px;background:linear-gradient(90deg,var(--coral),var(--coral-soft));color:#fff;font-size:8px;padding:15px 10px}
.select svg{position:absolute;right:14px;top:17px}
.note{left:267px;top:128px;width:160px;height:78px;border-radius:4px;background:#f0f0f0;font-size:8px;padding:9px 13px}
.total-time{left:267px;top:246px;width:160px;text-align:center;font-size:29px;font-weight:600}
.save{left:267px;top:289px;width:160px;height:39px;border-radius:4px;background:linear-gradient(90deg,var(--orange),var(--orange-soft));color:#fff;font-size:12px;font-weight:500;text-align:center;line-height:39px}
.today-title{left:15px;top:10px;font-size:13px;font-weight:500}
.chip{position:absolute;top:47px;width:30px;height:39px;border-radius:6px;background:#f6f6f8;text-align:center;font-size:10px;padding-top:6px;line-height:1.25}
.chip small{display:block;font-size:8px;font-weight:500}
.chip.on{background:var(--navy);color:#fff}
.dots{position:absolute;top:91px;display:flex;gap:2px;transform:translateX(-50%)}
.dots i{width:3.5px;height:3.5px;border-radius:50%}
.today-rule{left:97px;top:109px;width:30px;height:1.5px;background:var(--navy)}
.time-label{position:absolute;left:15px;font-size:7.5px;color:var(--muted)}
.time-line{position:absolute;left:45px;width:165px;height:1px;background:var(--line)}
.event{position:absolute;left:50px;width:160px;height:40px;border-radius:4px;color:#fff;padding:6px 6px 0 50px;font-size:8px;font-weight:500}
.event p{font-size:6.5px;font-weight:300;line-height:1.25}
.event .ico{position:absolute;left:6px;top:6px;width:28px;height:28px;border-radius:50%;background:#fff;display:flex;align-items:center;justify-content:center}
.ev-meet{background:linear-gradient(90deg,var(--coral),var(--coral-soft));box-shadow:0 6px 14px rgba(255,107,107,.3)}
.ev-check{background:linear-gradient(90deg,#2e2a6b,#8a88c0)}
.ev-course{background:linear-gradient(90deg,var(--orange),var(--orange-soft))}
.section-title{position:absolute;left:161px;font-size:18px;font-weight:500}
.btn{position:absolute;left:726px;width:122px;height:39px;border-radius:4px;color:#fff;font-size:12px;font-weight:500;line-height:39px}
.btn-coral{background:linear-gradient(90deg,var(--coral),var(--coral-soft));padding-left:25px}
.btn-coral svg{position:absolute;right:18px;top:16px}
.btn-orange{background:linear-gradient(90deg,var(--orange),var(--orange-soft));text-align:center}
.stat{top:545px;width:335px;height:182px}
.stat-left{left:161px}
.stat-right{left:514px}
.stat h3{position:absolute;left:21px;top:18px;font-size:14px;font-weight:500}
.legend{position:absolute;font-size:7.5px;display:flex;align-items:center;gap:5px;white-space:nowrap}
.legend i{width:6px;height:6px;border-radius:50%}
.legend .h{width:36px}
.legend .n{width:52px}
.donut{position:absolute}
.donut-label{position:absolute;text-align:center;width:100px}
.donut-label small{display:block;font-size:6.5px;color:#555}
.donut-label b{font-size:15px;font-weight:600}
.tasks-rule{left:158px;top:802px;width:100px;height:1px;background:#dcdce2}
.day-title{position:absolute;left:161px;font-size:14px;color:#8a8a94}
.task{position:absolute;width:327px;height:80px;border-radius:10px;background:#fafafa;box-shadow:0 4px 14px rgba(120,130,170,.06)}
.task .tile{position:absolute;left:16px;top:14px;width:54px;height:51px;border-radius:8px;display:flex;align-items:center;justify-content:center}
.task .tile svg{width:26px;height:26px;fill:none;stroke-width:1.6;stroke-linecap:round;stroke-linejoin:round}
.task h4{position:absolute;left:86px;top:20px;font-size:12.5px;font-weight:500}
.task .when{position:absolute;left:86px;top:42px;font-size:11.5px;color:#b5b5bd;font-weight:300}
.task .more{position:absolute;right:16px;top:30px;display:flex;flex-direction:column;gap:3px}
.task .more i{width:3.5px;height:3.5px;border-radius:50%;background:#6b6b75}
.tile-blue{background:#dbeafe}.tile-blue svg{stroke:#60a5fa}
.tile-peach{background:#fde5d0}.tile-peach svg{stroke:var(--orange)}
.tile-green{background:#dff3d8}.tile-green svg{stroke:#65b83f}
.tile-yellow{background:#fdf3cf}.tile-yellow svg{stroke:#f2c230}
</style>
</head>
<body>

<aside class="abs sidebar">
  <div class="nav-icon" style="top:66px"><svg viewBox="0 0 24 24"><circle cx="12" cy="12" r="9"/><path d="M12 7v5l3 2"/></svg></div>
  <div class="nav-icon" style="top:120px"><svg viewBox="0 0 24 24"><path d="M4 4v16h16"/><path d="M7 15l4-4 3 3 5-6"/></svg></div>
  <div class="nav-icon" style="top:186px"><svg viewBox="0 0 24 24"><path d="M20 11.5A8.5 8.5 0 1 1 15 4"/><path d="M8 11l3.5 3.5L21 5"/></svg></div>
  <div class="nav-icon" style="top:252px"><svg viewBox="0 0 24 24"><circle cx="12" cy="8" r="4.5"/><path d="M4 21c1-4.5 4-6.5 8-6.5s7 2 8 6.5"/></svg></div>
  <div class="nav-icon" style="top:1114px;left:29px"><svg viewBox="0 0 24 24"><path d="M14 4H5v16h9"/><path d="M10 12h11M17 8l4 4-4 4"/></svg></div>
</aside>

<header>
  <p class="abs greeting">Hello <b>LENA</b>, welcome back!</p>
  <h1 class="abs page-title">Track your time</h1>
  <svg class="abs bell" width="16" height="16" viewBox="0 0 24 24" fill="none" stroke="#9a9aa5" stroke-width="1.6" stroke-linecap="round"><path d="M6 16V11a6 6 0 0 1 12 0v5l2 2H4z"/><path d="M10 20a2 2 0 0 0 4 0"/></svg>
  <span class="abs bell-dot"></span>
  <div class="abs avatar" role="img" aria-label="User profile photo"></div>
  <p class="abs user-name">Lena Marsh</p>
  <p class="abs user-plan">Basic Plan</p>
  <svg class="abs user-chev" width="10" height="8" viewBox="0 0 10 8" fill="none" stroke="#26262e" stroke-width="1.6"><path d="M1 2l4 4 4-4"/></svg>
</header>

<section class="card tracker">
  <h2 class="abs cal-title">November, 2023</h2>
  <span class="abs cal-nav" style="left:185px">‹</span>
  <span class="abs cal-nav" style="left:218px">›</span>
  <div class="abs toggle"><span class="week">Week</span><span class="month">Month</span></div>

  <div class="day-head" style="left:36px;top:92px">Mon</div>
  <div class="day-head" style="left:69px;top:92px">Tue</div>
  <div class="day-head" style="left:103px;top:92px">Wed</div>
  <div class="day-head" style="left:137px;top:92px">Thu</div>
  <div class="day-head" style="left:166px;top:92px">Fri</div>
  <div class="day-head" style="left:195px;top:92px">Sat</div>
  <div class="day-head" style="left:226px;top:92px">Sun</div>

  <div class="day-num" style="left:103px;top:110px">1</div>
  <div class="day-num" style="left:137px;top:110px">2</div>
  <div class="day-num" style="left:166px;top:110px">3</div>
  <div class="day-num" style="left:195px;top:110px">4</div>
  <div class="day-num" style="left:226px;top:110px">5</div>
  <div class="day-num" style="left:36px;top:132px">6</div>
  <div class="day-num" style="left:69px;top:132px">7</div>
  <div class="day-num" style="left:103px;top:132px">8</div>
  <div class="day-num" style="left:137px;top:132px">9</div>
  <div class="day-num" style="left:166px;top:132px">10</div>
  <div class="day-num" style="left:195px;top:132px">11</div>
  <div class="day-num" style="left:226px;top:132px">12</div>
  <div class="day-num" style="left:36px;top:153px">13</div>
  <div class="day-num" style="left:69px;top:153px">14</div>
  <div class="day-num" style="left:103px;top:153px">15</div>
  <div class="day-num active" style="left:137px;top:152px">16</div>
  <div class="day-num" style="left:166px;top:153px">17</div>
  <div class="day-num" style="left:195px;top:153px">18</div>
  <div class="day-num" style="left:226px;top:153px">19</div>
  <div class="day-num" style="left:36px;top:175px">20</div>
  <div class="day-num" style="left:69px;top:175px">21</div>
  <div class="day-num" style="left:103px;top:175px">22</div>
  <div class="day-num" style="left:137px;top:175px">23</div>
  <div class="day-num" style="left:166px;top:175px">24</div>
  <div class="day-num" style="left:195px;top:175px">25</div>
  <div class="day-num" style="left:226px;top:175px">26</div>
  <div class="day-num" style="left:36px;top:194px">27</div>
  <div class="day-num" style="left:69px;top:194px">28</div>
  <div class="day-num" style="left:103px;top:194px">29</div>
  <div class="day-num" style="left:137px;top:194px">30</div>

  <div class="abs cal-rule"></div>

  <div class="dur sel" style="left:31px;top:233px">1h</div>
  <div class="dur" style="left:82px;top:233px">2h</div>
  <div class="dur" style="left:133px;top:233px">3h</div>
  <div class="dur" style="left:184px;top:233px">4h</div>
  <div class="dur" style="left:31px;top:263px">6h</div>
  <div class="dur" style="left:82px;top:263px">7h</div>
  <div class="dur" style="left:133px;top:263px">9h</div>
  <div class="dur" style="left:184px;top:263px">8h</div>
  <div class="dur" style="left:31px;top:302px">0m</div>
  <div class="dur sel" style="left:82px;top:302px">15m</div>
  <div class="dur" style="left:133px;top:302px">30m</div>
  <div class="dur" style="left:184px;top:302px">45m</div>

  <div class="abs select" style="top:30px">Select Project<svg width="7" height="5" viewBox="0 0 7 5" fill="none" stroke="#fff" stroke-width="1"><path d="M1 1l2.5 2.5L6 1"/></svg></div>
  <div class="abs select" style="top:79px">Select Type<svg width="7" height="5" viewBox="0 0 7 5" fill="none" stroke="#fff" stroke-width="1"><path d="M1 1l2.5 2.5L6 1"/></svg></div>
  <div class="abs note">What did you do?</div>
  <div class="abs total-time">1h 15m</div>
  <div class="abs save">Save</div>
</section>

<section class="card today">
  <h2 class="abs today-title">Today, 05 March</h2>
  <div class="chip" style="left:14px">03<small>Mon</small></div>
  <div class="chip" style="left:56px">04<small>Tue</small></div>
  <div class="chip on" style="left:97px">05<small>Wed</small></div>
  <div class="chip" style="left:139px">06<small>Thu</small></div>
  <div class="chip" style="left:180px">07<small>Fri</small></div>
  <div class="dots" style="left:29px"><i style="background:#f43f5e"></i><i style="background:var(--violet)"></i><i style="background:var(--teal)"></i></div>
  <div class="dots" style="left:71px"><i style="background:#f43f5e"></i></div>
  <div class="dots" style="left:112px"><i style="background:#f43f5e"></i><i style="background:var(--violet)"></i><i style="background:var(--teal)"></i></div>
  <div class="dots" style="left:154px"><i style="background:var(--violet)"></i></div>
  <div class="dots" style="left:195px"><i style="background:#f43f5e"></i><i style="background:var(--teal)"></i></div>
  <div class="abs today-rule"></div>

  <span class="time-label" style="top:117px">08 am</span><div class="time-line" style="top:122px"></div>
  <span class="time-label" style="top:167px">09 am</span><div class="time-line" style="top:198px"></div>
  <span class="time-label" style="top:218px">10 am</span>
  <span class="time-label" style="top:268px">11 am</span><div class="time-line" style="top:273px"></div>
  <span class="time-label" style="top:318px">12 pm</span>

  <div class="event ev-meet" style="top:147px">
    <span class="ico"><svg width="15" height="12" viewBox="0 0 24 18" fill="none" stroke="#26262e" stroke-width="2"><rect x="1" y="2" width="15" height="14" rx="3"/><path d="M16 7l6-4v12l-6-4"/></svg></span>
    Client Meeting<p>Design club client meeting to review the final deisgn</p>
  </div>
  <div class="event ev-check" style="top:222px">
    <span class="ico"><svg width="13" height="13" viewBox="0 0 24 24" fill="none" stroke="#26262e" stroke-width="2" stroke-linecap="round"><path d="M3 5l2 2 3-3M3 12l2 2 3-3M3 19l2 2 3-3M11 6h10M11 13h10M11 20h10"/></svg></span>
    Check List<p>Complete the tasks in the check list</p>
  </div>
  <div class="event ev-course" style="top:298px">
    <span class="ico"><svg width="13" height="13" viewBox="0 0 24 24" fill="none" stroke="#26262e" stroke-width="2" stroke-linejoin="round"><rect x="2" y="3" width="20" height="14" rx="2"/><path d="M6 8h8M6 12h5"/><circle cx="16" cy="15" r="3"/><path d="M14.5 18l-1 4 2.5-1.5 2.5 1.5-1-4"/></svg></span>
    Course<p>Complete the ongoing design course</p>
  </div>
</section>

<h2 class="section-title" style="top:495px">Statistics</h2>
<div class="btn btn-coral" style="top:488px">Monate<svg width="9" height="6" viewBox="0 0 9 6" fill="none" stroke="#fff" stroke-width="1.3"><path d="M1 1l3.5 3.5L8 1"/></svg></div>

<section class="card stat stat-left">
  <h3>Current Month</h3>
  <div class="legend" style="left:18px;top:120px"><i style="background:var(--blue)"></i><span class="h">40:45h</span><span>Customer A (89%)</span></div>
  <div class="legend" style="left:18px;top:143px"><i style="background:var(--amber)"></i><span class="h">10:00h</span><span>Customer B &nbsp; (11%)</span></div>
  <svg class="donut" style="left:180px;top:32px" width="118" height="118" viewBox="0 0 118 118">
    <g transform="rotate(-90 59 59)" fill="none" stroke-width="15">
      <circle cx="59" cy="59" r="50" stroke="var(--blue)" stroke-dasharray="312 2" stroke-dashoffset="0"/>
      <circle cx="59" cy="59" r="50" stroke="var(--amber)" stroke-dasharray="82 232" stroke-dashoffset="-190"/>
      <circle cx="59" cy="59" r="50" stroke="#fff" stroke-dasharray="2 312" stroke-dashoffset="-189"/>
      <circle cx="59" cy="59" r="50" stroke="#fff" stroke-dasharray="2 312" stroke-dashoffset="-272"/>
      <circle cx="59" cy="59" r="50" stroke="#fff" stroke-dasharray="2 312" stroke-dashoffset="-313"/>
    </g>
  </svg>
  <div class="donut-label" style="left:189px;top:77px"><small>Total</small><b>50:45h</b></div>
</section>

<section class="card stat stat-right">
  <h3 style="left:15px">November</h3>
  <div class="legend" style="left:16px;top:45px"><i style="background:var(--teal)"></i><span class="h">40:45h</span><span class="n">Customer A</span><span>(53%)</span></div>
  <div class="legend" style="left:16px;top:69px"><i style="background:var(--yellow)"></i><span class="h">10:00h</span><span class="n">Customer B</span><span>(13%)</span></div>
  <div class="legend" style="left:16px;top:92px"><i style="background:var(--amber)"></i><span class="h">20:00h</span><span class="n">Customer c</span><span>(34%)</span></div>
  <div class="legend" style="left:16px;top:115px"><i style="background:var(--pink)"></i><span class="h">22:45h</span><span class="n">Customer D</span><span>(53%)</span></div>
  <div class="legend" style="left:16px;top:139px"><i style="background:var(--violet)"></i><span class="h">02:15h</span><span class="n">Customer E</span><span>(13%)</span></div>
  <div class="legend" style="left:16px;top:162px"><i style="background:var(--blue)"></i><span class="h">20:00h</span><span class="n">Customer F</span><span>(34%)</span></div>
  <svg class="donut" style="left:176px;top:32px" width="116" height="116" viewBox="0 0 116 116">
    <g transform="rotate(-90 58 58)" fill="none" stroke-width="14">
      <circle cx="58" cy="58" r="49" stroke="var(--teal)" stroke-dasharray="109.8 198" stroke-dashoffset="0"/>
      <circle cx="58" cy="58" r="49" stroke="var(--blue)" stroke-dasharray="39 269" stroke-dashoffset="-111"/>
      <circle cx="58" cy="58" r="49" stroke="var(--violet)" stroke-dasharray="20.5 288" stroke-dashoffset="-151"/>
      <circle cx="58" cy="58" r="49" stroke="var(--pink)" stroke-dasharray="51 257" stroke-dashoffset="-172.5"/>
      <circle cx="58" cy="58" r="49" stroke="var(--amber)" stroke-dasharray="42 266" stroke-dashoffset="-224.5"/>
      <circle cx="58" cy="58" r="49" stroke="var(--yellow)" stroke-dasharray="39.4 269" stroke-dashoffset="-267.5"/>
    </g>
  </svg>
  <div class="donut-label" style="left:184px;top:74px"><small>Gesamt</small><b>114:00h</b></div>
</section>

<h2 class="section-title" style="top:770px">Your tasks</h2>
<div class="abs tasks-rule"></div>
<div class="btn btn-orange" style="top:764px">Filter</div>

<h3 class="day-title" style="top:814px">Wednesday</h3>
<article class="task" style="left:161px;top:849px">
  <div class="tile tile-blue"><svg viewBox="0 0 24 24"><path d="M2 5h7a3 3 0 0 1 3 3v12a2 2 0 0 0-2-2H2z"/><path d="M22 5h-7a3 3 0 0 0-3 3v12a2 2 0 0 1 2-2h8z"/></svg></div>
  <h4>Customer A – Project 1</h4><p class="when">8:00 AM – 10:00 AM</p>
  <div class="more"><i></i><i></i><i></i></div>
</article>
<article class="task" style="left:522px;top:849px">
  <div class="tile tile-peach"><svg viewBox="0 0 24 24"><path d="M15 4l5 5-10 10H5v-5z"/><path d="M4 22h16"/></svg></div>
  <h4>Customer B – Project 1</h4><p class="when">01:00 PM – 02:00 PM</p>
  <div class="more"><i></i><i></i><i></i></div>
</article>

<h3 class="day-title" style="top:954px">Tuesday</h3>
<article class="task" style="left:161px;top:989px">
  <div class="tile tile-blue"><svg viewBox="0 0 24 24"><path d="M2 5h7a3 3 0 0 1 3 3v12a2 2 0 0 0-2-2H2z"/><path d="M22 5h-7a3 3 0 0 0-3 3v12a2 2 0 0 1 2-2h8z"/></svg></div>
  <h4>Customer A – Project 1</h4><p class="when">8:00 AM – 10:00 AM</p>
  <div class="more"><i></i><i></i><i></i></div>
</article>
<article class="task" style="left:522px;top:989px">
  <div class="tile tile-peach"><svg viewBox="0 0 24 24"><path d="M15 4l5 5-10 10H5v-5z"/><path d="M4 22h16"/></svg></div>
  <h4>Customer B – Project 1</h4><p class="when">01:00 PM – 02:00 PM</p>
  <div class="more"><i></i><i></i><i></i></div>
</article>
<article class="task" style="left:163px;top:1082px">
  <div class="tile tile-green"><svg viewBox="0 0 24 24"><path d="M3 17v-4a9 9 0 0 1 18 0v4"/><rect x="3" y="14" width="4" height="7" rx="2"/><rect x="17" y="14" width="4" height="7" rx="2"/></svg></div>
  <h4>Customer A – Project 1</h4><p class="when">8:00 AM – 10:00 AM</p>
  <div class="more"><i></i><i></i><i></i></div>
</article>
<article class="task" style="left:524px;top:1082px">
  <div class="tile tile-yellow"><svg viewBox="0 0 24 24"><path d="M3 9h4l6-5v16l-6-5H3z"/><path d="M17 9a4 4 0 0 1 0 6"/></svg></div>
  <h4>Customer B – Project 1</h4><p class="when">01:00 PM – 02:00 PM</p>
  <div class="more"><i></i><i></i><i></i></div>
</article>

</body>
</html>
```